Artist business cards needed, happy acrylic painter

I'd like a business card I can hand out to people interested in my paintings. I'd like a logo that includes elements of my painting. I have shared a collection that may be used at https://snaplink.example/photos/7xQpLmR3Tz8vBn2K
I get my vibe and the type of art I create, you can also see my active Circle Net account: https://circlesnet.example/+MarlaVintner

Target Market(s)

people interested in art

Industry/Entity Type

Artists

Contact Information for Business Card

Marla Vintner
425-736-1048
marlavintner@quillpost.com
marlavintner@quillpost.com
www.marlavintner-studio.com

Font styles to use
Sans Serif
Decorative
Script

Requirements
Must have
• 1. Colors that are represented in my paintings
• 2. Elements from my paintings: Link to the cloud locker with my art: https://snaplink.example/photos/7xQpLmR3Tz8vBn2K
• 3. Flower(s)
• 4. A box on the back that's outlined so a note could be added. I've attached a photo of a business card my friend uses for her floral design company as an example of the back of the card with the quote and a box and business name (Marla Vintner).
• 4. I'd like to have this quote on the back of the card too.
• "I must have flowers, always and always."
• ~Anton Brisle
Nice to have
• In smaller font
• If it fits, links to my other social media:
• https://circlesnet.example/+MarlaVintner
• https://www.friendwall.example/marlavintnerartist/
Should not have
• A dark background

```html
<!DOCTYPE html>
<html lang="en">
<head>
<meta charset="utf-8">
<title>Marla Vintner – Business Cards</title>
<link rel="stylesheet" href="https://fonts.googleapis.com/css2?family=Sacramento&family=Sue+Ellen+Francisco&family=Arimo:wght@400;700&display=swap">
<style>
  :root {
    --plum: #6e1f5c;
    --magenta: #9a2a85;
    --banner: rgba(138, 48, 140, 0.62);
    --lavender: #b8a6d8;
    --lilac: #cfa9d6;
    --rose: #d99bc4;
    --leaf: #a9c995;
    --butter: #e8e3a4;
    --sky: #8fb4d8;
    --indigo: #5e63b3;
    --paper: #ffffff;
    --stage: #eeebe7;
    --ink: #5b1a4c;
  }
  * { box-sizing: border-box; margin: 0; padding: 0; }
  html, body { width: 1200px; height: 1200px; overflow: hidden; }
  body { background: var(--stage); position: relative; font-family: "Arimo", Arial, sans-serif; color: var(--ink); }

  .card { position: absolute; background: var(--paper); overflow: hidden; box-shadow: 0 3px 10px rgba(0,0,0,0.12); }
  .card--wide { width: 540px; height: 300px; }
  .card--tall { width: 300px; height: 540px; }
  .front-wide { left: 40px; top: 50px; }
  .back-wide { left: 620px; top: 200px; }
  .front-tall { left: 60px; top: 420px; }
  .back-tall { left: 430px; top: 580px; }

  .painting { position: absolute; left: 0; width: 100%; }
  .painting--lilac {
    background:
      radial-gradient(circle at 20% 30%, var(--butter) 0, transparent 28%),
      radial-gradient(circle at 70% 25%, var(--lilac) 0, transparent 35%),
      radial-gradient(circle at 85% 75%, var(--lavender) 0, transparent 40%),
      radial-gradient(circle at 15% 80%, var(--rose) 0, transparent 35%),
      linear-gradient(135deg, var(--leaf), var(--lavender) 55%, var(--lilac));
  }
  .painting--band {
    background:
      radial-gradient(ellipse at 15% 70%, #c9499a 0, transparent 35%),
      radial-gradient(ellipse at 55% 40%, var(--leaf) 0, transparent 30%),
      radial-gradient(ellipse at 90% 30%, var(--butter) 0, transparent 30%),
      linear-gradient(90deg, var(--lavender), var(--indigo) 45%, var(--sky));
  }
  .rule { position: absolute; left: 0; width: 100%; height: 3px; background: var(--plum); }

  .banner { position: absolute; background: var(--banner); border-radius: 6px; color: #fff; }
  .name { font-family: "Sacramento", cursive; font-weight: 400; line-height: 0.9; color: #fff; white-space: nowrap; }
  .site { font-weight: 700; letter-spacing: 0.04em; color: #fff; white-space: nowrap; }

  .contact { position: absolute; font-size: 13px; line-height: 1.5; color: var(--ink); }
  .social { display: flex; align-items: center; gap: 6px; font-size: 11px; line-height: 1.7; white-space: nowrap; }
  .social .dot { width: 12px; height: 12px; border-radius: 50%; background: var(--plum); flex: none; }

  .flower { position: absolute; width: 70px; height: 38px; border-radius: 40%;
    background: radial-gradient(circle at 35% 50%, #e7a6c8 0, #c86c9f 45%, transparent 70%),
                radial-gradient(circle at 70% 50%, #f3d2df 0, #d48db2 45%, transparent 70%); }
  .quote { position: absolute; font-family: "Sue Ellen Francisco", cursive; color: var(--magenta); line-height: 1.1; text-align: right; white-space: nowrap; }
  .attribution { position: absolute; font-size: 11px; line-height: 1; color: var(--ink); text-align: right; white-space: nowrap; }
  .notes { position: absolute; border: 1px solid var(--magenta); }
  .notes-label { position: absolute; top: -8px; left: 14px; padding: 0 5px; background: var(--paper); font-size: 11px; line-height: 14px; color: var(--ink); }
</style>
</head>
<body>

<!-- Front, landscape -->
<section class="card card--wide front-wide">
  <div class="painting painting--lilac" style="top:0;height:232px" role="img" aria-label="Detail of a lilac and pastel floral acrylic painting"></div>
  <div class="banner" style="left:30px;top:40px;width:445px;height:140px">
    <div class="name" style="position:absolute;left:22px;top:14px;font-size:92px">marla vintner</div>
    <div class="site" style="position:absolute;right:40px;bottom:12px;font-size:15px">www.marlavintner-studio.com</div>
  </div>
  <div class="rule" style="top:232px"></div>
  <div class="contact" style="left:14px;top:250px">425-736-1048<br>marlavintner@quillpost.com</div>
  <div class="contact" style="left:310px;top:242px">
    <div class="social"><span class="dot"></span>circlesnet.example/+MarlaVintner</div>
    <div class="social"><span class="dot"></span>friendwall.example/marlavintnerartist/</div>
  </div>
</section>

<!-- Back, landscape -->
<section class="card card--wide back-wide">
  <div class="flower" style="left:18px;top:10px" role="img" aria-label="Small painted pink flower"></div>
  <div class="quote" style="right:20px;top:6px;font-size:30px">“I must have flowers always &amp; always.”</div>
  <div class="attribution" style="right:24px;top:60px">~Anton Brisle</div>
  <div class="notes" style="left:26px;top:82px;width:486px;height:146px"><span class="notes-label">Notes</span></div>
  <div class="rule" style="top:242px"></div>
  <div class="painting painting--band" style="top:245px;height:55px" role="img" aria-label="Strip of a colourful floral acrylic painting"></div>
</section>

<!-- Front, portrait -->
<section class="card card--tall front-tall">
  <div class="painting painting--lilac" style="top:0;height:392px" role="img" aria-label="Detail of a lilac and pastel floral acrylic painting"></div>
  <div class="banner" style="left:22px;top:92px;width:256px;height:232px">
    <div class="name" style="position:absolute;left:24px;top:22px;font-size:86px">marla<br>vintner</div>
    <div class="site" style="position:absolute;left:0;right:0;bottom:14px;text-align:center;font-size:12px">www.marlavintner-studio.com</div>
  </div>
  <div class="rule" style="top:392px"></div>
  <div class="contact" style="left:0;right:0;top:408px;text-align:center;font-weight:700;font-size:14px">425-736-1048<br>marlavintner@quillpost.com</div>
  <div class="contact" style="left:40px;top:460px">
    <div class="social"><span class="dot"></span>circlesnet.example/+MarlaVintner</div>
    <div class="social"><span class="dot"></span>friendwall.example/marlavintnerartist/</div>
  </div>
</section>

<!-- Back, portrait -->
<section class="card card--tall back-tall">
  <div class="flower" style="left:30px;top:14px" role="img" aria-label="Small painted pink flower"></div>
  <div class="quote" style="right:22px;top:46px;font-size:29px">“I must have flowers<br>always &amp; always.”</div>
  <div class="attribution" style="right:24px;top:134px">~Anton Brisle</div>
  <div class="notes" style="left:28px;top:162px;width:244px;height:284px"><span class="notes-label">Notes</span></div>
  <div class="rule" style="top:462px"></div>
  <div class="painting painting--band" style="top:465px;height:75px" role="img" aria-label="Strip of a colourful floral acrylic painting"></div>
</section>

</body>
</html>
```